Torvin Electrics Flyer Design Advertising

I am after an A5 Flyer design to help promote my electrical services business.
I would like to have information on what my business offers, photos of electrical work, and specials/deals for an amount of time.

Industry/Entity Type

Electrician

Font styles to use
Sans Serif

Colors
0292cd
33a6d7
85cae6
3176b5
333333
1b1b1b
ffffff
5c5c5c
474747

Requirements
Must have
• Specialising in New homes, renovations and commercial projects
• Contact details:
• ph. 0457 613 948
• email admin@torvinelectrics.com.au
• facebook TorvinElectrics
• Specials/Deals:
• 10% off all electrical services
• or
• Free LED downlights on installation
• *Terms conditions apply
• ALL RESIDENTIAL & COMMERCIAL ELECTRICAL SERVICES
• - New Home installations
• - Commercial projects
• - Shop fit outs
• - Renovations
• - Smoke Detectors
• - Air Conditioning and Ceiling Fans
• - Garden Lighting
• - Oven and Cooktop Installations
• - Power Point installation
• - LED lighting upgrades
• - Security Lighting
• - Switchboard upgrades
• - Test and Tag
• - Commercial Property
• - General Electrical Maintenance

```html
<!DOCTYPE html>
<html lang="en">
<head>
<meta charset="utf-8">
<title>Torvin Electrics Flyer</title>
<link href="https://fonts.googleapis.com/css2?family=Titillium+Web:ital,wght@0,400;0,600;0,700;1,600;1,700&display=swap" rel="stylesheet">
<style>
  :root{
    --blue:#0292cd;
    --blue-mid:#33a6d7;
    --blue-light:#85cae6;
    --blue-deep:#3176b5;
    --charcoal:#333333;
    --ink:#1b1b1b;
    --white:#ffffff;
    --grey:#5c5c5c;
    --grey-dark:#474747;
    --paper:#e8e8e8;
    --stage:#eeeeee;
  }
  *{margin:0;padding:0;box-sizing:border-box}
  html,body{width:1200px;height:800px;overflow:hidden;background:var(--stage)}
  body{font-family:"Titillium Web",sans-serif;position:relative}
  .flyer{position:absolute;left:330px;top:18px;width:540px;height:764px;background:var(--paper);overflow:hidden;box-shadow:0 2px 10px rgba(0,0,0,.15)}
  .backdrop{position:absolute;inset:0}
  .brand{position:absolute;left:22px;top:32px;display:flex;align-items:center;gap:14px}
  .brand-dot{width:84px;height:84px;border-radius:50%;background:var(--blue)}
  .brand-name{font-size:30px;font-weight:700;color:var(--charcoal);line-height:1}
  .contact{position:absolute;left:372px;top:22px;font-size:15px;font-weight:700;color:var(--ink)}
  .contact-row{display:flex;align-items:center;gap:6px;height:26px}
  .contact-row svg{width:20px;height:20px}
  .photo{position:absolute;border-radius:50%;border:4px solid var(--white);box-shadow:0 1px 4px rgba(0,0,0,.25)}
  .photo-kitchen{left:20px;top:196px;width:108px;height:108px;background:radial-gradient(circle at 50% 40%,#f2efe9,#b9ac9c 70%,#6d6257)}
  .photo-interior{left:151px;top:146px;width:148px;height:148px;background:linear-gradient(160deg,#f4f4f2,#c9ccc8 55%,#7e857f)}
  .photo-patio{left:312px;top:90px;width:200px;height:200px;background:linear-gradient(180deg,#6a8bb8 0%,#9bb1cf 35%,#b98e5f 58%,#5f4a36 72%,#3f5a2e 100%)}
  .headline{position:absolute;left:0;top:304px;width:540px;text-align:center;color:var(--white);font-weight:700;font-size:30px;line-height:38px;text-transform:uppercase;text-shadow:0 1px 2px rgba(0,0,0,.25)}
  .services-band{position:absolute;left:0;top:431px;width:470px;height:37px}
  .services-band-title{position:absolute;left:75px;top:433px;font-size:17px;font-style:italic;font-weight:700;color:var(--charcoal);line-height:33px}
  .service-list{position:absolute;left:76px;top:478px;list-style:none;color:var(--white);font-size:12.5px;font-weight:700;line-height:15.7px}
  .service-list li{padding-left:15px;position:relative}
  .service-list li::before{content:"";position:absolute;left:0;top:6px;width:4px;height:4px;border-radius:50%;background:var(--white)}
  .deal{position:absolute;left:301px;top:560px;width:210px;height:140px;border:3px solid var(--white);border-radius:10px;color:var(--white);text-align:center}
  .deal-label{position:absolute;left:22px;top:-15px;height:24px;display:flex}
  .deal-label-tab{width:18px;background:var(--charcoal);clip-path:polygon(40% 0,100% 0,100% 100%,0 100%)}
  .deal-label-text{background:var(--paper);color:var(--ink);font-size:14px;font-weight:600;padding:0 10px;line-height:24px}
  .deal-big{font-size:28px;font-weight:700;line-height:30px}
  .deal-first{margin-top:18px}
  .deal-small{font-size:13px;line-height:16px}
  .deal-terms{font-size:9px;font-style:italic;margin-top:3px}
  .footer-email{position:absolute;left:0;top:718px;width:540px;height:46px;display:flex;align-items:center;justify-content:center;gap:8px;font-size:15px;font-weight:700;color:var(--ink)}
  .footer-email svg{width:22px;height:22px}
</style>
</head>
<body>
<main class="flyer">
  <svg class="backdrop" width="540" height="764" viewBox="0 0 540 764">
    <polygon points="0,242 540,106 540,124 0,260" fill="var(--charcoal)"/>
    <polygon points="0,257 540,121 540,720 0,720" fill="var(--blue)"/>
    <polygon points="0,431 470,431 455,468 0,468" fill="var(--paper)"/>
    <polygon points="0,431 72,431 57,468 0,468" fill="var(--charcoal)"/>
    <polygon points="0,720 72,720 50,764 0,764" fill="var(--charcoal)"/>
  </svg>

  <div class="brand">
    <span class="brand-dot"></span>
    <span class="brand-name">TORVIN ELECTRICS</span>
  </div>

  <div class="contact">
    <div class="contact-row">
      <svg viewBox="0 0 20 20"><circle cx="10" cy="10" r="9" fill="none" stroke="var(--blue)" stroke-width="1.5"/><path d="M7 5.5l2 2-1 1.3c.6 1.4 1.6 2.4 3 3l1.3-1 2 2-1.2 1.4c-3.5-.4-6.6-3.5-7-7z" fill="var(--blue)"/></svg>
      <span>0457 613 948</span>
    </div>
    <div class="contact-row">
      <svg viewBox="0 0 20 20"><circle cx="10" cy="10" r="9" fill="none" stroke="var(--blue)" stroke-width="1.5"/></svg>
      <span>TorvinElectrics</span>
    </div>
  </div>

  <div class="photo photo-kitchen" role="img" aria-label="Photo of a modern kitchen with bench stools and lighting"></div>
  <div class="photo photo-interior" role="img" aria-label="Photo of a bright open-plan interior with pendant lights"></div>
  <div class="photo photo-patio" role="img" aria-label="Photo of an outdoor patio lit with downlights at dusk"></div>

  <h1 class="headline">Specialising in<br>New Homes, Renovations &amp;<br>Commercial Projects</h1>

  <div class="services-band-title">All Residential &amp; Commercial Electrical Services</div>

  <ul class="service-list">
    <li>New Home installations</li>
    <li>Commercial projects</li>
    <li>Shop fit outs</li>
    <li>Renovations</li>
    <li>Smoke Detectors</li>
    <li>Air Conditioning and Ceiling Fans</li>
    <li>Garden Lighting</li>
    <li>Oven and Cooktop Installations</li>
    <li>Power Point installation</li>
    <li>LED lighting upgrades</li>
    <li>Security Lighting</li>
    <li>Switchboard upgrades</li>
    <li>Test and Tag</li>
    <li>Commercial Property</li>
    <li>General Electrical Maintenance</li>
  </ul>

  <section class="deal">
    <div class="deal-label"><span class="deal-label-tab"></span><span class="deal-label-text">Specials/Deals:</span></div>
    <div class="deal-big deal-first">10% off</div>
    <div class="deal-small">all electrical services or</div>
    <div class="deal-big">Free LED</div>
    <div class="deal-small">downlights on installation</div>
    <div class="deal-terms">*Terms conditions apply</div>
  </section>

  <div class="footer-email">
    <svg viewBox="0 0 22 22"><circle cx="11" cy="11" r="10" fill="none" stroke="var(--ink)" stroke-width="1.5"/><rect x="5.5" y="7" width="11" height="8" fill="none" stroke="var(--ink)" stroke-width="1.4"/><path d="M5.5 7l5.5 4.5L16.5 7" fill="none" stroke="var(--ink)" stroke-width="1.4"/></svg>
    <span>admin@torvinelectrics.com.au</span>
  </div>
</main>
</body>
</html>
```